Website Design For Ecommerce Brand That Sells Personalized Wall Decor

We need a new website for our company Copper Lantern. Our current site is functioning through wordpress/woocomerce but we are not happy with the appearance. Our products really wow people when they receive them and we need your help making our website do the same!

Number of Pages Required

4 page

```html
<!DOCTYPE html>
<html lang="en">
<head>
<meta charset="utf-8">
<title>Copper Lantern – Home Decor</title>
<link href="https://fonts.googleapis.com/css2?family=Libre+Baskerville:ital,wght@0,400;0,700;1,400&family=Questrial&family=Mulish:ital,wght@0,400;0,600;0,700;1,400;1,600&display=swap" rel="stylesheet">
<style>
:root{
  --header:#fcc8cb;
  --hero:#fbe8e9;
  --accent:#ef5a62;
  --accent-soft:#f7a1a6;
  --thumb:#fad4d6;
  --ink:#1b1b1b;
  --muted:#9a9a9a;
  --star:#f5c518;
  --line:#f6cfd1;
  --footer:#fdf6f6;
}
*{box-sizing:border-box;margin:0;padding:0}
html,body{width:1200px;height:2375px;overflow:hidden;background:#fff}
body{position:relative;font-family:"Mulish",sans-serif;color:var(--ink)}
.abs{position:absolute}
.serif{font-family:"Libre Baskerville",serif}
.gothic{font-family:"Questrial",sans-serif}

/* header */
.site-header{left:0;top:0;width:1200px;height:95px;background:var(--header);box-shadow:0 2px 4px rgba(0,0,0,.08)}
.brand{left:53px;top:28px;display:flex;align-items:center;gap:6px;font-family:"Questrial",sans-serif;font-size:15px;color:var(--ink);line-height:1}
.brand-mark{width:12px;height:12px;background:var(--ink);border-radius:50%}
.nav{top:34px;font-family:"Libre Baskerville",serif;font-size:17px}
.search{left:473px;top:26px;width:535px;height:39px;border:2px solid var(--ink);border-radius:20px;background:var(--header)}
.search span{position:absolute;left:26px;top:9px;font-family:"Libre Baskerville",serif;font-size:13.5px;color:#555}
.search svg{position:absolute;right:14px;top:9px}
.icons svg{position:absolute;top:37px}

/* hero */
.hero{left:0;top:95px;width:1200px;height:212px;background:var(--hero);border-bottom:1px solid #eee}
.hero h1{position:absolute;width:100%;top:72px;text-align:center;font-family:"Libre Baskerville",serif;font-size:44px;font-weight:700}

/* product */
.photo-card{left:53px;top:339px;width:486px;height:489px;background:#ececec;border-radius:14px;box-shadow:2px 2px 6px rgba(0,0,0,.15)}
.photo{left:77px;top:364px;width:437px;height:438px;background:radial-gradient(circle at 50% 45%,#5a4535 0%,#3b2d23 55%,#2b211a 100%);border:14px solid #b38b62}
.thumb{top:876px;width:74px;height:73px;background:var(--thumb)}
.p-title{left:591px;top:338px;width:520px;font-family:"Libre Baskerville",serif;font-weight:700;font-size:18.5px;line-height:25px}
.price{left:589px;top:404px;font-family:"Libre Baskerville",serif;font-weight:700;font-size:22px;color:var(--accent)}
.stars{left:706px;top:408px}
.review-count{left:838px;top:411px;font-family:"Libre Baskerville",serif;font-size:12px}
.rule{height:2px;background:var(--line)}
.tabs{left:591px;top:502px;width:565px;height:447px;border-radius:16px;box-shadow:1px 1px 5px rgba(0,0,0,.18);background:#fff}
.tab{position:absolute;top:16px;font-family:"Libre Baskerville",serif;font-weight:700;font-size:18px;color:var(--muted);padding-bottom:4px;border-bottom:2px solid #bbb}
.tab.active{color:var(--accent);border-color:var(--accent)}
.desc{position:absolute;left:26px;top:68px;width:500px;font-family:"Libre Baskerville",serif;font-size:10.3px;line-height:17.5px;color:#222}
.desc p{margin-bottom:17.5px}
.scrollbar{position:absolute;left:549px;top:366px;width:4px;height:31px;background:var(--accent);border-radius:2px}

/* personalize */
.h-form{font-family:"Questrial",sans-serif;font-size:20.5px;font-weight:700;-webkit-text-stroke:.4px var(--ink)}
.guide{left:54px;top:1135px;width:640px;font-family:"Questrial",sans-serif;font-size:15px;line-height:18.8px}
.guide .lead{font-size:18px;-webkit-text-stroke:.35px var(--ink);margin-bottom:18px}
.guide .note{font-family:"Mulish",sans-serif;font-style:italic;font-weight:600;font-size:14.5px;margin-bottom:38px}
.guide .ex-head{font-weight:700;-webkit-text-stroke:.3px var(--ink);margin-bottom:19px}
.guide p{margin-bottom:18.8px}
.guide .it{font-style:italic}
.hint{left:753px;top:1107px;font-family:"Questrial",sans-serif;font-size:15px}
.field{border:2px solid var(--accent);border-radius:6px;background:#fff;font-family:"Questrial",sans-serif;font-size:18px;color:#c4c4c4;padding-left:40px}
.qty{left:832px;top:1663px;width:133px;height:43px;border-radius:22px;background:var(--accent);color:#fff;font-family:"Questrial",sans-serif;font-weight:700;font-size:28px;display:flex;justify-content:space-around;align-items:center}
.cart{left:984px;top:1646px;width:171px;height:76px;border-radius:38px;background:var(--accent);color:#fff;font-family:"Questrial",sans-serif;font-size:22px;display:flex;justify-content:center;align-items:center}

/* footer */
.footer{left:0;top:1823px;width:1200px;height:552px;background:var(--footer);border-top:2px solid #e9e9e9}
.touch{left:0;width:1200px;text-align:center}
.touch h2{font-family:"Libre Baskerville",serif;font-weight:700;font-size:52px}
.touch p{font-family:"Questrial",sans-serif;font-size:30px}
.email{left:88px;top:2032px;width:1007px;height:69px;border-radius:35px;background:#f9e2e3;box-shadow:0 2px 4px rgba(0,0,0,.12)}
.email span{position:absolute;left:49px;top:20px;font-family:"Questrial",sans-serif;font-size:24px}
.notify{position:absolute;right:0;top:0;width:234px;height:69px;border-radius:35px;background:var(--accent-soft);font-family:"Questrial",sans-serif;font-weight:700;font-size:30px;display:flex;align-items:center;justify-content:center;letter-spacing:1px;color:#222}
.pay{top:2159px;width:111px;height:60px;border-radius:6px;background:#fff;box-shadow:1px 2px 4px rgba(0,0,0,.2);display:flex;align-items:center;justify-content:center;font-family:"Questrial",sans-serif;font-size:18px;color:var(--ink)}
.links{left:0;top:2262px;width:1200px;text-align:center;font-family:"Libre Baskerville",serif;font-weight:700;font-size:14px;word-spacing:1px}
.copy{left:0;top:2305px;width:1200px;text-align:center;font-family:"Questrial",sans-serif;font-weight:700;font-size:13px}
</style>
</head>
<body>

<header class="abs site-header">
  <div class="abs brand"><span class="brand-mark"></span>Copper Lantern</div>
  <a class="abs nav" style="left:205px">Shop</a>
  <a class="abs nav" style="left:287px">FAQ</a>
  <a class="abs nav" style="left:359px">Contact</a>
  <div class="abs search"><span>Search anything you want...</span>
    <svg width="20" height="20" viewBox="0 0 20 20"><circle cx="8" cy="8" r="6" fill="none" stroke="#1b1b1b" stroke-width="2.4"/><line x1="12.5" y1="12.5" x2="18" y2="18" stroke="#1b1b1b" stroke-width="2.6" stroke-linecap="round"/></svg>
  </div>
  <div class="icons">
    <svg style="left:1054px" width="16" height="17" viewBox="0 0 16 17"><circle cx="8" cy="5" r="4" fill="#1b1b1b"/><path d="M1 17c0-5 3-7 7-7s7 2 7 7z" fill="#1b1b1b"/></svg>
    <svg style="left:1085px" width="19" height="17" viewBox="0 0 19 17"><path d="M9.5 16 2 8.5A4.5 4.5 0 0 1 9.5 3a4.5 4.5 0 0 1 7.5 5.5z" fill="#1b1b1b"/></svg>
    <svg style="left:1116px" width="19" height="17" viewBox="0 0 19 17"><path d="M0 1h3l2.5 10h10l2-7H5" fill="none" stroke="#1b1b1b" stroke-width="2"/><path d="M5 4h13l-2 7H6z" fill="#1b1b1b"/><circle cx="7" cy="15" r="1.6" fill="#1b1b1b"/><circle cx="15" cy="15" r="1.6" fill="#1b1b1b"/></svg>
  </div>
</header>

<section class="abs hero"><h1>Home Decor</h1></section>

<div class="abs photo-card"></div>
<div class="abs photo" role="img" aria-label="Framed wooden family tree wall art with name hearts on a dark wood backdrop"></div>
<div class="abs thumb" style="left:96px"></div>
<div class="abs thumb" style="left:194px"></div>
<div class="abs thumb" style="left:292px"></div>
<div class="abs thumb" style="left:391px"></div>

<h2 class="abs p-title">12 Inch Square Framed Personalized Family Tree Wall Decor</h2>
<div class="abs price">$62.00</div>
<svg class="abs stars" width="114" height="20" viewBox="0 0 114 20">
  <g fill="#f5c518">
    <path id="st" d="M9 1l2.4 5.6 6 .5-4.6 4 1.4 5.9L9 14l-5.2 3 1.4-5.9-4.6-4 6-.5z"/>
    <use href="#st" x="23"/><use href="#st" x="46"/><use href="#st" x="69"/><use href="#st" x="92"/>
  </g>
</svg>
<div class="abs review-count">01 Review</div>
<div class="abs rule" style="left:591px;top:463px;width:564px"></div>

<div class="abs tabs">
  <span class="tab active" style="left:26px">Description</span>
  <span class="tab" style="left:189px">Additional Info</span>
  <span class="tab" style="left:393px">Review</span>
  <div class="desc">
    <p>RUSTIC WOODEN FAMILY TREE ARTWORK FOR YOUR WALL – Add a great unique special touch to your home with our wooden carved family tree, elegantly framed and featuring the custom names of everyone you love regalos para abuela gifts</p>
    <p>PERSONALIZED WITH NAMES OF FAMILY MEMBERS – The leaves of the tree are interspersed with wooden hearts, each one displaying the name of another family member in a classy cursive font arbol genealogico para pared</p>
    <p>THE PERFECT PRESENT FOR A WEDDING OR ANNIVERSARY – Gift your parents, grandparents, or favorite couple a personalized canvas they can proudly display in their sitting rooms. Meaningful and unique, our family name wall art is a great way to celebrate couples’ anniversaries or weddings</p>
    <p>INTRICATE WORKMANSHIP AND PREMIUM QUALITY – The personalized wall art is laser cut onto a wooden backdrop with exquisite attention to detail. Handmade and surrounded with a dark wood frame, this piece of art is a refined take on the classic family names print</p>
    <p>CUSTOMIZED TO SUIT EVERY FAMILY – Whether you’d like to add the beloved family pets onto the tree or request a special design for a loved one that’s passed, we’ll work to create a family tree uniquely suited to your clan</p>
  </div>
  <div class="scrollbar"></div>
</div>

<div class="abs rule" style="left:54px;top:1014px;width:1101px"></div>

<h3 class="abs h-form" style="left:54px;top:1067px">Personalize Your Tree Below *</h3>
<div class="abs guide">
  <div class="lead">Enter all names you would like on the hearts along with description:</div>
  <div class="note">Please Separate By Pressing “ENTER” on your keyboard:<br>Special Instructions Feel Free To Email Us Directly</div>
  <div class="ex-head">Perfect Example How To Explain Hearts To Us:</div>
  <p>Middle of tree: (2” heart/ grandparents): Bob &amp; Sue</p>
  <p>Family 1: John (kid) Mary (spouse)<br>Mike, Stacy (Mike’s Spouse), Beth, Jackson (grandkids)<br>Mason (great grand kid-son of Mike and Stacy)<br>Rover, Spot (dogs)</p>
  <p>Family 2: Jennifer (kid) Lou (spouse)<br>Riley, Kristen, Lilly (grandkids)<br>Max (dog)</p>
  <p>Family 3: Matt (kid)<br>Sandra (grandkid)<br>Midnight, Sam (cats)</p>
  <p class="it">• Item can also be shipped without placement IF you so choose<br>to attach the hearts yourself. Hearts are easily attached with wood glue.</p>
  <p class="it">• Don’t forget we will reach out with a photo for approval and if you<br>would like that to be in a text on your cell then leave your number in the<br>Notes section.</p>
</div>

<h3 class="abs h-form" style="left:753px;top:1067px">Headline *</h3>
<div class="abs hint">“Grandkids”, “Our Family”, “The Smiths”</div>
<div class="abs field" style="left:754px;top:1159px;width:402px;height:53px;line-height:49px">Type here...</div>
<div class="abs field" style="left:754px;top:1261px;width:402px;height:358px;padding-top:36px">Describe here...</div>
<div class="abs qty"><span>-</span><span>01</span><span>+</span></div>
<div class="abs cart">Add to cart</div>

<footer class="abs footer"></footer>
<div class="abs touch" style="top:1882px"><h2>Get In Touch</h2></div>
<div class="abs touch" style="top:1940px"><p>Don't miss latest updates &amp; hot deals</p></div>
<div class="abs email"><span>email here...</span><div class="notify">notify me</div></div>
<div class="abs pay" style="left:393px">Cardwell</div>
<div class="abs pay" style="left:541px">Paystream</div>
<div class="abs pay" style="left:689px">Vantix</div>
<div class="abs links">Home &nbsp;|&nbsp; Home Decor &nbsp;|&nbsp; Gnome &nbsp;|&nbsp; Personalized Gifts &nbsp;|&nbsp; Craft Supplies &nbsp;|&nbsp; Pre-Cut Shapes &nbsp;|&nbsp; Unfinished Wood &nbsp;|&nbsp; Halloween</div>
<div class="abs copy">Copyright 2022 © Copper Lantern</div>

</body>
</html>
```